Threshold
Business cards/letter head
Threshold - Consulting
Creative Brief
Use standard fonts
Maren Holt
3187 Wexbury Ave NE Seattle, WA 98115
Holt.maren@quillpost.example
please use a complementary font to the logo. logo art uploaded.

```html
<!DOCTYPE html>
<html lang="en">
<head>
<meta charset="utf-8">
<title>Threshold Group – Business Cards</title>
<link href="https://fonts.googleapis.com/css2?family=Montserrat:wght@300;400;600&display=swap" rel="stylesheet">
<style>
  :root {
    --backdrop: #5b4e40;
    --card-dark: #4a4a4c;
    --card-dark-map: #5c5c5f;
    --card-light: #ffffff;
    --ink: #555558;
    --ink-soft: #7a7a7d;
    --ink-on-dark: #e9e9ea;
    --accent: #e2c72c;
    --band: #5a5a5d;
  }
  * { box-sizing: border-box; margin: 0; padding: 0; }
  html, body { width: 1200px; height: 904px; overflow: hidden; }
  body {
    background: var(--backdrop);
    font-family: "Montserrat", Arial, sans-serif;
    position: relative;
  }
  .card {
    position: absolute;
    width: 620px;
    height: 354px;
    border-radius: 4px;
    overflow: hidden;
    box-shadow: 0 14px 30px rgba(0,0,0,.35);
  }
  .card--front { left: 170px; top: 80px; background: var(--card-dark); }
  .card--back  { left: 410px; top: 470px; background: var(--card-light); }

  .world-map {
    position: absolute;
    left: 70px; top: 20px;
    width: 480px; height: 314px;
    border-radius: 50%;
    background: radial-gradient(ellipse at center, var(--card-dark-map) 0%, rgba(92,92,95,.6) 55%, rgba(74,74,76,0) 75%);
  }

  .brand { position: absolute; display: flex; flex-direction: column; align-items: flex-end; }
  .brand__mark {
    width: 34px; height: 34px; border-radius: 50%;
    background: var(--accent);
    margin-right: 52px; margin-bottom: 4px;
  }
  .brand__name { font-weight: 300; font-size: 40px; line-height: 1; letter-spacing: .5px; }
  .brand__sub  { font-weight: 300; font-size: 17px; line-height: 1.1; }

  .card--front .brand { left: 200px; top: 118px; color: var(--ink-on-dark); }

  .card--back .brand { left: 44px; top: 120px; color: var(--ink); }

  .divider {
    position: absolute; left: 340px; top: 104px;
    width: 1px; height: 120px; background: var(--ink-soft);
  }
  .contact { position: absolute; left: 362px; top: 110px; color: var(--ink); font-size: 12.5px; line-height: 1.45; }
  .contact__name { color: var(--accent); font-weight: 600; font-size: 15px; margin-bottom: 6px; }
  .contact__address { margin-bottom: 10px; }
  .contact__row { display: flex; align-items: center; gap: 8px; }
  .contact__row svg { width: 13px; height: 13px; flex: none; }

  .accent-line {
    position: absolute; left: 0; right: 0; top: 296px; height: 3px; background: var(--accent);
  }
  .footer-band {
    position: absolute; left: 0; right: 0; bottom: 0; height: 42px; background: var(--band);
  }
  .footer-dashes { position: absolute; left: 0; right: 0; top: 312px; height: 4px; }
</style>
</head>
<body>
  <section class="card card--front">
    <div class="world-map" role="img" aria-label="Faint world map behind the logo"></div>
    <div class="brand">
      <span class="brand__mark"></span>
      <span class="brand__name">threshold</span>
      <span class="brand__sub">group</span>
    </div>
  </section>

  <section class="card card--back">
    <div class="brand">
      <span class="brand__mark"></span>
      <span class="brand__name">threshold</span>
      <span class="brand__sub">group</span>
    </div>
    <div class="divider"></div>
    <div class="contact">
      <p class="contact__name">Maren Holt</p>
      <p class="contact__address">3187 Wexbury Ave NE<br>Seattle, WA 98115</p>
      <p class="contact__row">
        <svg viewBox="0 0 16 16"><rect x="4" y="1" width="8" height="14" rx="1.5" fill="none" stroke="var(--accent)" stroke-width="1.8"/></svg>
        +1 206-555-0142
      </p>
      <p class="contact__row">
        <svg viewBox="0 0 16 16"><rect x="1" y="3" width="14" height="10" fill="var(--accent)"/><path d="M1 3l7 6 7-6" fill="none" stroke="#fff" stroke-width="1.4"/></svg>
        Holt.maren@quillpost.example
      </p>
    </div>
    <div class="accent-line"></div>
    <svg class="footer-dashes" viewBox="0 0 620 4" preserveAspectRatio="none">
      <rect x="0" y="0" width="300" height="4" fill="var(--band)"/>
      <rect x="312" y="0" width="40" height="4" fill="var(--accent)"/>
      <rect x="362" y="0" width="18" height="4" fill="var(--accent)"/>
      <rect x="390" y="0" width="230" height="4" fill="var(--band)"/>
    </svg>
    <div class="footer-band"></div>
  </section>
</body>
</html>
```